Banners for slider on first page of the website

We need up to 3 different banners for our website: www.trelk.si
Current design is maybe a bit too playful, so do not mind on it. It can include some natural elements
1) Design needs to be modern type
2) Has to include products which are on our website
3) Has to be in two sizes: mobile and web - like we have now
4) Each slider CAN represent each category we have or CAN include multiple
5) Optional text holders

```html
<!DOCTYPE html>
<html lang="sl">
<head>
<meta charset="utf-8">
<title>Trelk – slider banner</title>
<link rel="stylesheet" href="https://fonts.googleapis.com/css2?family=Poppins:wght@600&display=swap">
<style>
  :root {
    --pink-deep: #e0669a;
    --pink-mid: #f08dbb;
    --pink-light: #fbc3dd;
    --glow: #fff4fa;
    --podium-top: #fbd0e2;
    --podium-side: #f4a3c6;
    --podium-shade: #ea8db6;
    --arc: #ffffff;
  }
  * { margin: 0; padding: 0; box-sizing: border-box; }
  html, body { width: 1200px; height: 466px; overflow: hidden; }
  body { font-family: "Poppins", sans-serif; }
  .banner {
    position: relative;
    width: 1200px;
    height: 466px;
    overflow: hidden;
    background:
      radial-gradient(ellipse 420px 300px at 870px 120px, rgba(255,244,250,.85), rgba(255,244,250,0) 70%),
      radial-gradient(ellipse 520px 260px at 260px 40px, rgba(251,195,221,.75), rgba(251,195,221,0) 70%),
      linear-gradient(180deg, var(--pink-mid) 0%, #f49cc4 55%, #f08ab8 78%, var(--pink-mid) 100%);
  }
  .banner::after {
    content: "";
    position: absolute; inset: 0;
    background: linear-gradient(90deg, rgba(224,102,154,.35) 0%, rgba(224,102,154,0) 25%, rgba(224,102,154,0) 80%, rgba(224,102,154,.45) 100%);
    pointer-events: none;
  }
  .stage { position: absolute; inset: 0; }
  .product {
    position: absolute;
    box-shadow: 0 4px 8px rgba(160,40,100,.18);
  }
  .product--cupcake-red   { left: 586px; top: 230px; width: 88px;  height: 88px; border-radius: 50%; background: radial-gradient(circle at 45% 35%, #f6a04a, #e03c4f 70%); }
  .product--cupcake-yellow{ left: 655px; top: 192px; width: 74px;  height: 110px; border-radius: 45% 45% 20% 20%; background: linear-gradient(180deg, #fff6d6 0%, #fbe77a 55%, #f2d23a 100%); }
  .product--shell         { left: 635px; top: 260px; width: 80px;  height: 60px;  border-radius: 50% 50% 30% 30%; background: linear-gradient(180deg, #7fe0ec, #2fb7d4); }
  .product--tub-lilac     { left: 730px; top: 74px;  width: 98px;  height: 188px; border-radius: 48% 48% 12% 12%; background: linear-gradient(180deg, #d2479a 0%, #b0508f 38%, #c9b8f0 50%, #a89de6 100%); }
  .product--panda         { left: 840px; top: 106px; width: 112px; height: 160px; border-radius: 50% 50% 14% 14%; background: linear-gradient(180deg, #ffffff 0%, #f2f2f8 58%, #b58de6 62%, #9d7ad8 100%); }
  .product--rainbow-ball  { left: 776px; top: 176px; width: 86px;  height: 94px;  border-radius: 50%; background: linear-gradient(180deg, #f34fb0 0%, #c46ad4 45%, #3ab8e6 100%); }
  .product--tub-pink      { left: 973px; top: 170px; width: 100px; height: 196px; border-radius: 48% 48% 10% 10%; background: linear-gradient(180deg, #e53b4d 0%, #5fc24a 22%, #ee2f86 42%, #e0226f 100%); }
  .product--unicorn       { left: 1056px; top: 230px; width: 98px; height: 136px; border-radius: 50% 50% 16% 16%; background: linear-gradient(180deg, #fffbf2 0%, #fbefd8 55%, #f44e9a 62%, #e83a87 100%); }
</style>
</head>
<body>
<main class="banner">
  <svg class="stage" width="1200" height="466" viewBox="0 0 1200 466" aria-hidden="true">
    <defs>
      <filter id="arc-glow" x="-20%" y="-20%" width="140%" height="140%">
        <feGaussianBlur stdDeviation="6" result="b"/>
        <feMerge><feMergeNode in="b"/><feMergeNode in="SourceGraphic"/></feMerge>
      </filter>
      <linearGradient id="podium-side" x1="0" y1="0" x2="1" y2="0">
        <stop offset="0" stop-color="#f6b2cf"/>
        <stop offset=".5" stop-color="#f8bcd6"/>
        <stop offset="1" stop-color="#ee97bf"/>
      </linearGradient>
    </defs>

    <path class="glow-arc" d="M600 330 A262 262 0 0 1 1124 330" fill="none" stroke="#ffffff" stroke-width="6" filter="url(#arc-glow)" opacity=".95"/>

    <ellipse cx="864" cy="440" rx="330" ry="18" fill="#d9669b" opacity=".25"/>

    <g class="podium podium--left">
      <rect x="575" y="318" width="156" height="108" fill="url(#podium-side)"/>
      <ellipse cx="653" cy="426" rx="78" ry="10" fill="#f2a8c8"/>
      <ellipse cx="653" cy="318" rx="78" ry="10" fill="#fcd6e6"/>
    </g>
    <g class="podium podium--right">
      <rect x="966" y="366" width="187" height="58" fill="url(#podium-side)"/>
      <ellipse cx="1059" cy="424" rx="93" ry="12" fill="#f2a8c8"/>
      <ellipse cx="1059" cy="366" rx="93" ry="12" fill="#fcd6e6"/>
    </g>
    <g class="podium podium--center">
      <rect x="728" y="262" width="238" height="174" fill="url(#podium-side)"/>
      <ellipse cx="847" cy="436" rx="119" ry="13" fill="#f2a8c8"/>
      <ellipse cx="847" cy="262" rx="119" ry="13" fill="#fcd6e6"/>
    </g>
  </svg>

  <div class="product product--tub-lilac" role="img" aria-label="Lilac bath melt tub topped with sprinkles and a number candle"></div>
  <div class="product product--panda" role="img" aria-label="White and lilac bath cupcake decorated as a panda"></div>
  <div class="product product--rainbow-ball" role="img" aria-label="Pink and blue bath bomb with a rainbow on top"></div>
  <div class="product product--cupcake-red" role="img" aria-label="Red bath bomb with summer sprinkles"></div>
  <div class="product product--cupcake-yellow" role="img" aria-label="Yellow bath cupcake with a bee decoration"></div>
  <div class="product product--shell" role="img" aria-label="Blue shell-shaped bath bomb"></div>
  <div class="product product--tub-pink" role="img" aria-label="Pink thank-you bath tub topped with green sprinkles"></div>
  <div class="product product--unicorn" role="img" aria-label="Pink bath cupcake with a unicorn decoration"></div>
</main>
</body>
</html>
```